Harvest Smokehouse League

The current website is hslsmoke.com. We want to change the color scheme to the gold/white and black in the logo. Front page elements include everything we have except the social media links at the top can go to the bottom. We need to add fliers like http://hslsmoke.com/content/fliers/2022/SmartSelect_20211215-123241_Slides.jpg to the front page. There are more available on the events page. Also a place for a main news story on the front page. All the sponsor logos need to be present on every page. I have added a couple of more sponsor logos. On the about us page we will want to add a contact list and email form. We will take care of all functionality. You provide only design.
One site we like is tpgr.us for it is easy to navigate.
Target Market(s)
People interested in competition BBQ
Coding
Number of Pages Required
5+ page
Look and feel

```html
<!DOCTYPE html>
<html lang="en">
<head>
<meta charset="utf-8">
<title>Harvest Smokehouse League</title>
<link href="https://fonts.googleapis.com/css2?family=Jost:wght@400;500;600&family=Libre+Baskerville:wght@700&display=swap" rel="stylesheet">
<style>
:root{
  --black:#000;
  --ink:#111;
  --gold:#e8a317;
  --gold-soft:#b09659;
  --gold-light:#f5dc8a;
  --gold-deep:#c9a24a;
  --white:#fff;
  --line:#d9d9d9;
  --bar:#232323;
}
*{margin:0;padding:0;box-sizing:border-box}
html,body{width:763px;height:1200px;overflow:hidden}
body{position:relative;background:var(--white);font-family:'Jost',sans-serif;color:var(--ink)}
.abs{position:absolute}

/* hero */
.hero{left:0;top:0;width:763px;height:302px;background:var(--black);overflow:hidden}
.hero-fire{left:0;top:0;width:763px;height:302px;
  background:
   radial-gradient(ellipse 160px 110px at 700px 280px,rgba(214,94,18,.75),transparent 70%),
   radial-gradient(ellipse 200px 90px at 360px 300px,rgba(170,70,15,.55),transparent 70%),
   radial-gradient(ellipse 120px 140px at 80px 250px,rgba(120,40,10,.45),transparent 70%),
   radial-gradient(ellipse 140px 80px at 720px 90px,rgba(150,55,12,.35),transparent 70%),
   linear-gradient(#050302,#1a0b04)}
.brand{left:60px;top:15px;font-weight:600;font-size:10px;letter-spacing:.6px;color:var(--gold-deep);text-transform:uppercase;white-space:nowrap}
.brand-dot{display:inline-block;width:9px;height:9px;border-radius:50%;background:var(--gold);vertical-align:-1px;margin-right:5px}
.nav{top:16px;display:flex;font-size:7.3px;font-weight:500;text-transform:uppercase;color:var(--gold)}
.nav span{position:absolute;white-space:nowrap}
.nav .active{color:#e8d6b0}
.quote{left:189px;top:62px;color:var(--white);font-weight:600;font-size:14px}
.quote small{display:block;font-size:9px;font-weight:500;margin-top:1px}
.headline{left:128px;top:120px;color:var(--white);font-family:'Libre Baskerville',serif;font-weight:700;font-size:29px;line-height:38px}
.where{left:128px;top:207px;color:var(--white);font-size:9px;font-weight:500;line-height:12px}
.progress{left:128px;top:254px;width:183px;height:1px;background:var(--gold-deep)}
.count{left:319px;top:248px;color:var(--white);font-size:9.5px}
.flyer{left:477px;top:62px;width:160px;height:222px;
  background:radial-gradient(ellipse 60px 70px at 80px 140px,#f08a1c,transparent 75%),linear-gradient(#4a3526,#2a1c12 60%,#3a2418);
  box-shadow:0 0 18px rgba(0,0,0,.8)}

/* sponsors */
.sponsors{left:0;top:302px;width:763px;height:219px;background:var(--gold-soft)}
.section-title{width:763px;text-align:center;font-weight:600;font-size:18px;left:0}
.sponsors .section-title{top:36px;color:var(--white);letter-spacing:.5px}
.tile{top:77px;width:85px;height:72px;display:flex;align-items:center;justify-content:center;text-align:center;font-size:9px;font-weight:600;padding:4px}
.tile.dark{background:#000;color:var(--gold)}
.tile.light{background:var(--white);color:#2a2a2a}
.tile.navy{background:#0f1a28;color:#e6e6e6}
.dots{top:168px;left:358px;display:flex;gap:3px}
.dots i{width:7px;height:7px;border:1px solid var(--white);border-radius:50%;display:block;position:relative}
.dots i.on::after{content:"";position:absolute;left:1.5px;top:1.5px;width:2px;height:2px;border-radius:50%;background:var(--white)}

/* team of the year */
.toy-title{top:556px;color:var(--ink)}
.tabs{left:187px;top:596px;width:390px;height:20px;display:flex;border-radius:10px;overflow:hidden;font-size:7.5px}
.tabs span{flex:1;display:flex;align-items:center;justify-content:center;background:linear-gradient(#e4e4e4,#c8c8c8);border-left:1px solid #b5b5b5}
.tabs span.on{background:linear-gradient(var(--gold-light),var(--gold-deep));border-left:0}
.panel{left:128px;top:617px;width:509px;height:321px;border:1px solid var(--line)}
.panel-title{top:12px;left:0;width:507px;text-align:center;font-size:11.5px;font-weight:500}
.standings{position:absolute;left:58px;top:39px;width:391px;border-collapse:collapse;font-size:7px;font-weight:500;text-align:center}
.standings th{height:32px;font-weight:500;font-size:7.8px;background:linear-gradient(var(--gold-light),var(--gold-deep));border-right:1px solid #c9b06a}
.standings td{height:19.1px;border:1px solid var(--line);letter-spacing:.2px}
.see-all{left:226px;top:283px;width:56px;height:16px;border:1px solid var(--gold-soft);border-radius:8px;font-size:7.5px;color:var(--gold-soft);display:flex;align-items:center;justify-content:center}

/* footer */
.footer{left:0;top:978px;width:763px;height:205px;background:var(--black);color:var(--white)}
.footer .brand{left:130px;top:45px;font-size:8px;letter-spacing:.3px}
.footer .brand-dot{width:8px;height:8px;margin-right:4px}
.f-line{font-size:8px;line-height:12px}
.f-head{font-weight:600;font-size:12px;letter-spacing:.3px}
.social{width:20px;height:20px;border:1px solid var(--white);border-radius:50%}
.signup{left:477px;top:122px;width:160px;height:20px;background:var(--white);border-radius:10px;overflow:hidden;display:flex}
.signup .field{flex:1;font-size:6.5px;color:#555;padding-left:12px;display:flex;align-items:center}
.signup .submit{width:46px;background:linear-gradient(var(--gold-deep),#b8902e);color:var(--ink);font-size:7.5px;font-weight:500;display:flex;align-items:center;justify-content:center}
.legal{left:0;top:1183px;width:763px;height:17px;background:var(--bar);color:var(--white);font-size:6px;display:flex;align-items:center;justify-content:center}
.legal b{color:var(--gold);font-weight:500;margin:0 2px}
</style>
</head>
<body>

<header class="abs hero">
  <div class="abs hero-fire" role="img" aria-label="Background photo of barbecue flames"></div>
  <div class="abs brand"><span class="brand-dot"></span>Harvest Smokehouse League</div>
  <nav class="abs nav" style="left:0">
    <span class="active" style="left:284px">Home</span>
    <span style="left:329px">Events</span>
    <span style="left:380px">Results +</span>
    <span style="left:440px">About HSL</span>
    <span style="left:504px">Members</span>
    <span style="left:561px">Sanctioning Form</span>
    <span style="left:659px">Contact Us</span>
  </nav>
  <p class="abs quote">"Let's make barbecue fun again!"<small>- Dale Whitaker</small></p>
  <h1 class="abs headline">Cedar Bend Rodeo &amp;<br>BBQ Cook-Off</h1>
  <p class="abs where">Cedar Bend, TX<br>Jan 29</p>
  <div class="abs progress"></div>
  <div class="abs count">01/04</div>
  <svg class="abs" style="left:59px;top:163px" width="22" height="22" viewBox="0 0 22 22"><circle cx="11" cy="11" r="10" fill="none" stroke="#fff"/><path d="M12.5 7 8.5 11l4 4" fill="none" stroke="#fff" stroke-width="1.1"/></svg>
  <svg class="abs" style="left:683px;top:163px" width="22" height="22" viewBox="0 0 22 22"><circle cx="11" cy="11" r="10" fill="none" stroke="#fff"/><path d="M9.5 7l4 4-4 4" fill="none" stroke="#fff" stroke-width="1.1"/></svg>
  <div class="abs flyer" role="img" aria-label="Event flier for the 2022 Cedar Bend Rodeo and BBQ Cook-Off with flames and ribs on a wood background"></div>
</header>

<section class="abs sponsors">
  <h2 class="abs section-title">Our Sponsors</h2>
  <div class="abs tile dark" style="left:60px">Redfox Rubs</div>
  <div class="abs tile light" style="left:153px">Prairie Meat Co.</div>
  <div class="abs tile light" style="left:246px;color:#2b3f8f">Bayou Sauce</div>
  <div class="abs tile dark" style="left:339px">Ironside Smokers</div>
  <div class="abs tile navy" style="left:432px">Caliche Vodka</div>
  <div class="abs tile dark" style="left:525px">KR BBQ</div>
  <div class="abs tile light" style="left:618px">Ranchline Steel</div>
  <div class="abs dots"><i></i><i class="on"></i><i></i><i></i><i></i></div>
</section>

<h2 class="abs section-title toy-title">Team of the Year</h2>
<div class="abs tabs"><span class="on">Overall</span><span>Chicken</span><span>Ribs</span><span>Pork</span><span>Brisket</span></div>
<section class="abs panel">
  <h3 class="abs panel-title">Overall</h3>
  <table class="standings">
    <colgroup><col style="width:78px"><col style="width:156px"><col style="width:78px"><col style="width:79px"></colgroup>
    <thead><tr><th>Rank</th><th>Team</th><th>Points</th><th style="border-right:0">Contest</th></tr></thead>
    <tbody>
      <tr><td>1</td><td>Mesquite Mike's BBQ</td><td>1491</td><td>3</td></tr>
      <tr><td>2</td><td>Los Halcones</td><td>1253</td><td>3</td></tr>
      <tr><td>3</td><td>Ember Born Grillers</td><td>1215</td><td>3</td></tr>
      <tr><td>4</td><td>Uncle Ray's BBQ</td><td>1075</td><td>3</td></tr>
      <tr><td>5</td><td>Holloway's BBQ</td><td>983</td><td>3</td></tr>
      <tr><td>6</td><td>Black Kettle Cookers</td><td>941</td><td>3</td></tr>
      <tr><td>7</td><td>Lone Pecan Heat BBQ</td><td>777</td><td>3</td></tr>
      <tr><td>8</td><td>Straight Shot BBQ Ortega Family</td><td>753</td><td>3</td></tr>
      <tr><td>9</td><td>Barbecue</td><td>743</td><td>3</td></tr>
      <tr><td>10</td><td>Bluebonnet Q</td><td>738</td><td>3</td></tr>
    </tbody>
  </table>
  <div class="abs see-all">See All</div>
</section>

<footer class="abs footer">
  <div class="abs brand"><span class="brand-dot"></span>Harvest Smokehouse League</div>
  <svg class="abs" style="left:129px;top:91px" width="9" height="11" viewBox="0 0 9 11"><path d="M4.5 10.5S1 6.5 1 4.2a3.5 3.5 0 0 1 7 0C8 6.5 4.5 10.5 4.5 10.5z" fill="none" stroke="#fff" stroke-width=".9"/><circle cx="4.5" cy="4.2" r="1.2" fill="none" stroke="#fff" stroke-width=".8"/></svg>
  <p class="abs f-line" style="left:147px;top:87px">1820 Saddlebrook Ln,<br>Mercer, TX 78412</p>
  <svg class="abs" style="left:128px;top:122px" width="11" height="11" viewBox="0 0 11 11"><path d="M2.2 1l2 2.2-1 1.3a6 6 0 0 0 3.3 3.3l1.3-1 2.2 2-1 1.2C5.4 10 1 5.6 1 2.2z" fill="none" stroke="#fff" stroke-width=".9"/></svg>
  <p class="abs f-line" style="left:144px;top:121px">(555) 014-2298</p>
  <div class="abs social" style="left:127px;top:146px"></div>
  <div class="abs social" style="left:151px;top:146px"></div>
  <div class="abs social" style="left:175px;top:146px"></div>
  <div class="abs social" style="left:199px;top:146px"></div>

  <h4 class="abs f-head" style="left:302px;top:49px">About Us</h4>
  <p class="abs f-line" style="left:302px;top:86px;width:150px">Harvest Smokehouse League is an organization founded by barbecue cooks for barbecue cooks and our main goal is to bring competition barbecue out of the stone age and into the information age... but above all we want to make barbecue fun again!</p>

  <h4 class="abs f-head" style="left:477px;top:49px">Be Informed</h4>
  <p class="abs f-line" style="left:477px;top:86px;width:150px">Get email notifications about events in your area</p>
  <div class="abs signup"><span class="field">Enter your email...</span><span class="submit">Submit</span></div>
</footer>
<div class="abs legal">© 2022 <b>Harvest Smokehouse League.</b> All Rights Reserved</div>

</body>
</html>
```